Leadership Brenvale Brochure Design*

We host a local leadership development program every two years. We need a brochure to promote the program. We would like it to be 8 1/2 x 11, tri-fold. I have attached a Word document with the necessary info for the brochure. The brochure will be professionally printed. We would like the final design to be in InDesign.

Target Market(s)

Potential participants of our leadership program. They will be local leaders, male and female, from 30-60 years of age.

Requirements
Must have
• Content as detailed in the Word document attached. Our logo.
Nice to have
• A design that is attractive to young professionals.

```html
<!DOCTYPE html>
<html lang="en">
<head>
<meta charset="utf-8">
<title>Leadership Brenvale – Program Brochure</title>
<link rel="stylesheet" href="https://fonts.googleapis.com/css2?family=Tinos:wght@400;700&family=Open+Sans:ital,wght@1,400&family=Pathway+Gothic+One&family=Arimo:wght@400;700&display=swap">
<style>
  :root{
    --paper:#ffffff;
    --ink:#1a1a1a;
    --accent-orange:#f29a2e;
    --band-grey:#c9d3da;
    --brand-blue:#1f2fc4;
    --photo-grey-light:#b9b9b9;
    --photo-grey-dark:#6f6f6f;
  }
  *{box-sizing:border-box;margin:0;padding:0}
  html,body{width:1200px;height:933px;overflow:hidden;background:var(--paper)}
  .brochure{position:relative;width:1200px;height:933px;background:var(--paper);color:var(--ink)}

  .top-band{position:absolute;left:0;top:0;width:400px;height:65px;background:var(--band-grey)}

  /* Left panel */
  .info-panel{position:absolute;left:46px;top:122px;width:346px;text-align:center;font-family:"Tinos",serif;font-size:13.3px;line-height:1.22}
  .info-panel h2{font-weight:400;font-size:13.3px;color:var(--accent-orange);margin:0 0 14px}
  .info-panel p{margin:0 0 14px}
  .info-panel .alumni-quote{margin-bottom:0}
  .info-panel .alumni-name{margin-top:0}

  /* Middle panel */
  .photo{position:absolute;background:linear-gradient(160deg,var(--photo-grey-light),var(--photo-grey-dark))}
  .photo-primary{left:560px;top:86px;width:101px;height:133px}
  .photo-secondary{left:425px;top:800px;width:113px;height:121px}
  .testimonial{position:absolute;left:444px;top:258px;width:312px;font-family:"Open Sans",sans-serif;font-style:italic;font-size:11.4px;line-height:1.45}
  .testimonial-credit{position:absolute;left:444px;top:498px;width:312px;font-family:"Tinos",serif;font-size:11.4px;line-height:1.35}
  .testimonial-credit .firm{display:block;padding-left:10px}
  .editor-note{position:absolute;left:592px;top:716px;width:190px;font-family:"Tinos",serif;font-size:19px;line-height:1.22;text-align:center}

  /* Right panel */
  .program-name{position:absolute;left:826px;top:82px;display:flex;align-items:center;gap:12px;font-family:"Arimo",sans-serif;font-weight:700;font-size:31px;line-height:1.05;color:var(--brand-blue)}
  .program-name .mark{width:26px;height:26px;border-radius:50%;background:var(--brand-blue);flex:none}
  .leadership-quote{position:absolute;left:840px;top:312px;width:312px;text-align:center;font-family:"Pathway Gothic One",sans-serif;font-size:41px;line-height:1.27}
  .sponsors{position:absolute;left:837px;top:849px;font-family:"Arimo",sans-serif;font-size:13px;line-height:1.3}
</style>
</head>
<body>
<main class="brochure">
  <div class="top-band"></div>

  <section class="info-panel">
    <h2>Attendance Policy</h2>
    <p>Attendance at all sessions including the opening retreat is compulsory. Participants may miss no more than one session to graduate; however, the Organizational Retreat is mandatory.</p>

    <h2>Tuition</h2>
    <p>If accepted in the Leadership Brenvale program, you or your employer/sponsor will be invoiced $400 for Chamber members and $500 for non-members. This fee covers costs for the retreat, classroom sessions, lunches, and graduation. No refunds will be provided for participants who drop out of the program or do not fulfill the required curriculum.</p>

    <h2>To Apply</h2>
    <p>Applications are available on the Chamber’s website, www.TheBrenvaleChamber.com Applications are due by November 2, 2020. Class size is limited. All applications received by the deadline will be reviewed and final participants for the Leadership Brenvale class will be contacted on December 4, 2020. However, all applicants will be notified of the status of their application in writing.</p>
    <p>For questions, please call the Chamber, 555-018-2740.</p>

    <h2>What Community alumni are saying</h2>
    <p class="alumni-quote">“Leadership Brenvale was an awesome experience! I learned many interesting things about the county that I have lived in all my life. We had very informative panel discussions and the tours of local attractions, including the Ridgeway Correctional Facility were eye opening! I enjoyed learning and working beside a great group of folks who are taking leadership roles in our communities to make our county a better place to live, work and play.”</p>
    <p class="alumni-name">Jolene Parrish, Co-Owner, Parrish Smokehouse</p>
  </section>

  <div class="photo photo-primary" role="img" aria-label="Portrait photo of program alumnus"></div>

  <blockquote class="testimonial">“For the first year and a half I was working at R. Whitcombe Hale, I commuted from Harborview, so I was not involved in the community at all. Once we moved here, I knew I wanted and felt I had to become more involved. I learned about the program through a colleague. I couldn’t have asked for a better experience and it really exposed me to the many ways that I could get involved and contribute to the chamber and our community. I didn’t know a soul in that 2014 class when it started and now many of them are my very best friends. If you have an opportunity to go through Leadership Brenvale you would be crazy to pass it up. It is the best program the Chamber has and, quite frankly, one of the best opportunities to better yourself in this community.”</blockquote>
  <p class="testimonial-credit">-Daniel R. Ashford, CPA, Partner/Manager of the Millbrook Office<span class="firm">R. Whitcombe Hale &amp; Partners, LLP</span></p>

  <div class="photo photo-secondary" role="img" aria-label="Portrait photo of program alumnus"></div>
  <p class="editor-note">*We may want to have one or two more testimonials if needed.</p>

  <div class="program-name"><span class="mark"></span><span>LEADERSHIP<br>BRENVALE</span></div>

  <blockquote class="leadership-quote">“The greatest wealth of a community lies not in the amount of its treasure, but in the quality of its leadership.”</blockquote>

  <p class="sponsors">Sponsored by:<br>Eastfield Community College<br>Brenvale Chamber of Commerce and Tourism</p>
</main>
</body>
</html>
```